Personalised Poetry business needs a business card designed

I am a writer that specialises in personalised poetry for people for significant life events.
I want a business card that stands out and portrays class and professionalism but is also welcoming & indicates warmth and honesty.
I'm happy with the logo that was designed for me, I would like to see it in raised print on the business card. I am open to suggestions on colours but think perhaps gold or silver writing for the logo would look good. I would like just the logo and my name and contact details on the front of the card. On the back of the card, I would like a list of the different events I provide poems for I will upload a photo of my current business card for reference. My current logo has a shading behind it that I don't like, I just want the words of the logo without any background colour

Target Market(s)

People wanting to provide a unique gift to someone special in their life

Industry/Entity Type

Writer

Contact Information for Business Card

Logo, my name and contact details on the front and a list of all the events I write poetry for on the back

Font styles to use
Script

Requirements
Must have
• I would like to see the logo, if possible, in a raised type of print on the card so that you can feel the actual words. I would like to have a glossy finish to the card and be able to print it on good quality board
Should not have
• The shading that is currently behind the logo on my current business card

```html
<!DOCTYPE html>
<html lang="en">
<head>
<meta charset="UTF-8">
<title>Lines for Always – Business Card</title>
<link rel="stylesheet" href="https://fonts.googleapis.com/css2?family=Great+Vibes&family=Montserrat:wght@400;500;700&display=swap">
<style>
  :root {
    --backdrop: #c7cbd1;
    --card-front: #fdf8f8;
    --card-back: #ffffff;
    --ink: #2f2f2f;
    --ink-soft: #3c3c3c;
    --shadow: rgba(40, 45, 55, 0.25);
  }
  * { box-sizing: border-box; margin: 0; padding: 0; }
  html, body {
    width: 1200px;
    height: 675px;
    overflow: hidden;
  }
  body {
    background: var(--backdrop);
    display: flex;
    align-items: center;
    justify-content: center;
    gap: 60px;
    font-family: "Montserrat", sans-serif;
    color: var(--ink);
  }
  .card {
    width: 520px;
    height: 300px;
    border-radius: 3px;
    box-shadow: 0 12px 30px var(--shadow);
    position: relative;
    overflow: hidden;
  }

  /* Front */
  .card--front {
    background: var(--card-front);
    padding: 48px 46px;
  }
  .brand {
    display: flex;
    align-items: center;
    gap: 14px;
  }
  .brand__name {
    font-weight: 500;
    font-size: 32px;
    color: var(--ink);
    letter-spacing: 0.5px;
  }
  .brand__mark {
    width: 18px;
    height: 18px;
    border-radius: 50%;
    background: var(--ink);
  }
  .contact {
    position: absolute;
    left: 46px;
    bottom: 44px;
  }
  .contact__name {
    font-weight: 700;
    font-size: 24px;
    margin-bottom: 14px;
  }
  .contact__phone {
    font-size: 16px;
    letter-spacing: 4px;
    margin-bottom: 6px;
  }
  .contact__email {
    font-size: 16px;
  }

  /* Back */
  .card--back {
    background: var(--card-back);
    padding: 28px 34px 0 38px;
  }
  .events__title {
    font-family: "Great Vibes", cursive;
    font-size: 28px;
    line-height: 36px;
    font-weight: 400;
    color: var(--ink-soft);
    margin-bottom: 10px;
  }
  .events__list {
    list-style: none;
  }
  .events__item {
    position: relative;
    padding-left: 18px;
    font-weight: 500;
    font-size: 18px;
    line-height: 34px;
    color: var(--ink-soft);
    white-space: nowrap;
  }
  .events__item::before {
    content: "•";
    position: absolute;
    left: 0;
    top: 0;
  }
</style>
</head>
<body>
  <section class="card card--front" aria-label="Card front">
    <div class="brand">
      <span class="brand__name">Lines for Always</span>
      <span class="brand__mark" aria-hidden="true"></span>
    </div>
    <div class="contact">
      <p class="contact__name">Marcus Hale</p>
      <p class="contact__phone">0400 555 123</p>
      <p class="contact__email">marcus@linesforalways.com</p>
    </div>
  </section>

  <section class="card card--back" aria-label="Card back">
    <h2 class="events__title">Momentous Life Events Personalised in Poetry</h2>
    <ul class="events__list">
      <li class="events__item">Weddings &amp; Anniversaries</li>
      <li class="events__item">Birthdays &amp; Christmas</li>
      <li class="events__item">Valentines Day</li>
      <li class="events__item">Retirements, Business &amp; Corporate Events</li>
      <li class="events__item">Funerals &amp; Eulogies</li>
    </ul>
  </section>
</body>
</html>
```